Hispanic Financial Counseling and Advocate Firm seeks business card design

Looking for a clean, professional business card design. This is a firm that specializes in providing financial education, coaching, and planning to the Hispanic community. The name of the company is Valemar, which means to prosper. We need a design that is clean, professional, and invokes trust, professionalism, but also welcoming. Our logo is a plant growing from a hand to give the messaging of of being in control of growing your financial future and security. Its part of a larger organization names Celesta Financial Group, who's logo is a tree with multi colored branches. We have the back of the card designed so we just need the front designed. the back is blue, so front needs to be a different background color, not blue.

Target Market(s)

Hispanic Community looking to better their future

Industry/Entity Type

financial services

Contact Information for Business Card

contact info: Anselmo Ibarra Jr, 951-555-0147, info@celestafinancialgroup.example. Celestafinancialgroup.example. tag line: Para un futuro mas seguro!

Requirements
Must have
• basics: logo, contact info.
Nice to have
• possibly incorporate the tree logo provided somehow
Should not have
• should not look like the back, needs to be different from the back provided.

```html
<!DOCTYPE html>
<html lang="es">
<head>
<meta charset="utf-8">
<title>Celesta Financial Group – Business Card</title>
<link href="https://fonts.googleapis.com/css2?family=Source+Sans+3:wght@400;700&display=swap" rel="stylesheet">
<style>
  :root {
    --page-bg: #e4e4e4;
    --card-bg: #f5f5f5;
    --sky: #2a9fd6;
    --navy: #153a55;
    --red: #e0464a;
    --green: #9cc33a;
    --yellow: #e3b51c;
    --purple: #a181bb;
    --text: #1f3a4f;
  }
  * { margin: 0; padding: 0; box-sizing: border-box; }
  html, body {
    width: 1200px; height: 900px; overflow: hidden;
    background: var(--page-bg);
    font-family: "Source Sans 3", "Myriad Pro", sans-serif;
  }
  .card {
    position: absolute; left: 150px; top: 193px;
    width: 900px; height: 514px;
    background: var(--card-bg);
    box-shadow: 0 6px 18px rgba(0,0,0,0.12);
    overflow: hidden;
  }
  .band-top { position: absolute; left: 0; top: 0; width: 100%; height: 26px; background: var(--sky); }
  .band-bottom { position: absolute; left: 0; bottom: 0; width: 100%; height: 36px; background: var(--navy); }
  .tab { position: absolute; width: 28px; height: 84px; }
  .tab-red { left: 20px; top: 132px; background: var(--red); }
  .tab-green { left: 20px; top: 292px; background: var(--green); }
  .tab-yellow { right: 20px; top: 62px; background: var(--yellow); }
  .tab-purple { right: 20px; top: 218px; background: var(--purple); }
  .brand {
    position: absolute; left: 90px; top: 170px; width: 300px;
    display: flex; flex-direction: column; align-items: center; gap: 16px;
    text-align: center;
  }
  .brand-dot { width: 64px; height: 64px; border-radius: 50%; background: var(--navy); }
  .brand-name { font-size: 26px; font-weight: 700; color: var(--navy); line-height: 1.15; }
  .divider { position: absolute; left: 415px; top: 70px; width: 2px; height: 330px; background: var(--red); }
  .contact { position: absolute; left: 462px; top: 72px; color: var(--text); }
  .contact-name { font-size: 36px; font-weight: 700; color: var(--navy); line-height: 1.1; }
  .contact-role { font-size: 22px; color: var(--sky); margin-top: 2px; }
  .contact-lines { list-style: none; margin-top: 40px; font-size: 22px; line-height: 34px; }
  .tagline { margin-top: 28px; font-size: 22px; color: var(--red); }
</style>
</head>
<body>
  <article class="card">
    <div class="band-top"></div>
    <div class="tab tab-red"></div>
    <div class="tab tab-green"></div>
    <div class="tab tab-yellow"></div>
    <div class="tab tab-purple"></div>

    <div class="brand">
      <span class="brand-dot"></span>
      <span class="brand-name">Celesta Financial Group</span>
    </div>

    <div class="divider"></div>

    <section class="contact">
      <h1 class="contact-name">Anselmo Ibarra Jr</h1>
      <p class="contact-role">CEO</p>
      <ul class="contact-lines">
        <li>951-555-0147</li>
        <li>info@celestafinancialgroup.example</li>
        <li>Celestafinancialgroup.example</li>
      </ul>
      <p class="tagline">Para un futuro mas seguro!</p>
    </section>

    <div class="band-bottom"></div>
  </article>
</body>
</html>
```